Envelope Design - Winner can do follow-up business

- Varindo.com is a Swiss-based online store selling business shirts and accessories for business men
- Please visit the webpage to make yourself familiar with the company. Although the text is in German, with Google translator you should be able to understand the main content.
- Our clients are mainly business men between 30 and 60 years old. Mostly with a high income working in the service industry (banking, insurance, lawyers, etc.). Sometimes there wives purchase the shirts for them ;-)
- The colors and the logo are given, as they are also used for the print materials (please see files in attachment)
- I am running several businesses and often need a talented web designer --> the winner gets substantial follow-up business
your task:
-for our company we need a new envelope design
-It should be simple and modern
-please use one of the logos in the followings.
-suprise me :)

```html
<!DOCTYPE html>
<html lang="en">
<head>
<meta charset="utf-8">
<title>Varindo Envelope</title>
<link rel="stylesheet" href="https://fonts.googleapis.com/css2?family=Montserrat:wght@400;500&display=swap">
<style>
  :root {
    --bg: #e9e9e9;
    --paper: #ffffff;
    --red: #e31b13;
    --gold: #e6c84c;
    --window: #acacac;
    --window-edge: #8f8f8f;
  }
  html, body {
    margin: 0;
    padding: 0;
    width: 1200px;
    height: 928px;
    overflow: hidden;
    background: var(--bg);
    font-family: "Montserrat", sans-serif;
  }
  .canvas {
    position: relative;
    width: 1200px;
    height: 928px;
  }
  .envelope {
    position: absolute;
    left: 140px;
    width: 920px;
    height: 400px;
    background: var(--paper);
    box-shadow: 0 2px 10px rgba(0,0,0,0.12);
    overflow: hidden;
  }
  .envelope--front { top: 40px; }
  .envelope--back { top: 488px; }
  .envelope svg.decor {
    position: absolute;
    inset: 0;
    width: 100%;
    height: 100%;
  }
  .address-window {
    position: absolute;
    left: 70px;
    top: 62px;
    width: 330px;
    height: 140px;
    border-radius: 22px;
    background: var(--window);
    border: 2px solid var(--window-edge);
    box-sizing: border-box;
  }
  .brand {
    position: absolute;
    display: flex;
    align-items: center;
    gap: 12px;
    font-weight: 500;
    letter-spacing: 0.22em;
  }
  .brand__mark {
    width: 14px;
    height: 14px;
  }
  .envelope--front .brand {
    right: 60px;
    bottom: 62px;
    font-size: 38px;
    color: var(--gold);
  }
  .envelope--front .brand__mark { background: var(--gold); width: 18px; height: 18px; }
  .envelope--back .brand {
    left: 46px;
    top: 96px;
    font-size: 24px;
    color: var(--red);
  }
  .envelope--back .brand__mark { background: var(--red); }
  .sender {
    position: absolute;
    left: 46px;
    top: 140px;
    margin: 0;
    font-style: normal;
    font-size: 11px;
    line-height: 1.5;
    color: var(--red);
  }
  .contact-email {
    position: absolute;
    right: 60px;
    bottom: 46px;
    font-size: 11px;
    color: var(--red);
  }
</style>
</head>
<body>
<main class="canvas">

  <section class="envelope envelope--front" aria-label="Envelope front">
    <svg class="decor" viewBox="0 0 920 400" aria-hidden="true">
      <line x1="0" y1="222" x2="250" y2="222" stroke="var(--red)" stroke-width="2"/>
      <line x1="250" y1="226" x2="920" y2="226" stroke="var(--gold)" stroke-width="2"/>
    </svg>
    <div class="address-window"></div>
    <div class="brand"><span class="brand__mark"></span>VARINDO</div>
  </section>

  <section class="envelope envelope--back" aria-label="Envelope back">
    <svg class="decor" viewBox="0 0 920 400" aria-hidden="true">
      <path class="flap" d="M60 0 C130 60 280 110 470 135 L800 168 Q920 182 920 140 L920 0 Z" fill="var(--red)"/>
      <line x1="0" y1="212" x2="290" y2="212" stroke="var(--red)" stroke-width="2"/>
      <line x1="290" y1="216" x2="920" y2="216" stroke="var(--gold)" stroke-width="2"/>
    </svg>
    <div class="brand"><span class="brand__mark"></span>VARINDO</div>
    <address class="sender">
      Musterstrasse 12<br>
      8000 Zurich<br>
      +41 44 000 00 00
    </address>
    <span class="contact-email">info@varindo.com</span>
  </section>

</main>
</body>
</html>
```